General Contractor Company introduction and presentation

i need a company presentation design for a construction company called R3 Construction Corp. we build brand ground up affordable apartment building as well Remodeling of apartment units and commercial buildings.
company was established in June 2020.

```html
<!DOCTYPE html>
<html lang="en">
<head>
<meta charset="utf-8">
<title>R3 Construction Corp. – Company Presentation</title>
<link href="https://fonts.googleapis.com/css2?family=Poppins:ital,wght@0,400;0,500;0,600;0,700;1,400&family=Oswald:wght@600;700&display=swap" rel="stylesheet">
<style>
:root{
  --green:#79d94f;
  --green-dark:#5fc23a;
  --ink:#2b2b2b;
  --gray-dark:#555;
  --gray:#8a8a8a;
  --gray-light:#b9b9b9;
  --panel:#ececec;
  --bg:#dedede;
  --white:#fff;
}
*{margin:0;padding:0;box-sizing:border-box}
html,body{width:1041px;height:1200px;overflow:hidden}
body{background:var(--bg);font-family:"Poppins",sans-serif;color:var(--ink)}
.deck{position:relative;width:1041px;height:1200px}
.slide{position:absolute;width:310px;height:174px;background:var(--white);overflow:hidden;box-shadow:0 2px 5px rgba(0,0,0,.18)}
.c1{left:39px}.c2{left:366px}.c3{left:692px}
.r1{top:36px}.r2{top:225px}.r3{top:415px}.r4{top:606px}.r5{top:799px}.r6{top:990px}
.abs{position:absolute}
.photo{position:absolute;background:linear-gradient(160deg,#d2d2d2,#7d7d7d 60%,#4e4e4e)}
.photo.light{background:linear-gradient(160deg,#e6e6e6,#a8a8a8 70%,#8a8a8a)}
.green{background:var(--green)}
.stripe{position:absolute;background:var(--green)}
.page{position:absolute;right:9px;bottom:6px;font-size:4px;color:var(--ink)}
.tiny{font-size:3.3px;line-height:1.35;color:var(--gray)}
.h-slide{font-weight:700;font-size:10.5px;line-height:1.15;color:var(--ink)}
.accent{display:block;width:12px;height:1.6px;background:var(--green);margin-top:3px;position:relative}
.accent::after{content:"";position:absolute;left:14px;top:0;width:3px;height:1.6px;background:var(--ink)}
.g{color:var(--green)}
.w{color:var(--white)}
.bold{font-weight:700}
.semi{font-weight:600}
.icon-ring{position:absolute;border-radius:50%;display:flex;align-items:center;justify-content:center}
</style>
</head>
<body>
<div class="deck">

<!-- 1 Cover -->
<section class="slide c1 r1">
  <div class="abs green" style="left:6px;top:6px;width:8px;height:8px"></div>
  <div class="abs" style="left:22px;top:28px;display:flex;align-items:center;gap:3px">
    <span style="width:6px;height:6px;background:var(--green);display:block"></span>
    <span style="font-size:4.2px;font-weight:600;color:var(--ink)">R3 Construction Corp.</span>
  </div>
  <div class="abs" style="left:18px;top:66px;font-family:'Oswald',sans-serif;font-weight:700;font-size:26px;line-height:1;color:var(--green)">BUSINESS</div>
  <div class="abs" style="left:18px;top:97px;font-size:12.5px;letter-spacing:.3px;color:var(--gray-dark)">MARKETING</div>
  <div class="abs" style="left:18px;top:114px;width:8px;height:1.4px;background:var(--green)"></div>
  <div class="abs" style="left:28px;top:114px;width:3px;height:1.4px;background:var(--ink)"></div>
  <div class="abs" style="left:18px;top:119px;font-size:7.5px;font-style:italic;color:var(--gray-dark)">Presentation</div>
  <div class="abs tiny" style="left:18px;top:130px;width:80px;font-style:italic">Building affordable homes and remodeling spaces since June 2020.</div>
  <div class="abs" style="left:19px;top:156px;display:flex;gap:3px">
    <i style="width:3px;height:3px;border-radius:50%;background:var(--gray-dark);display:block"></i>
    <i style="width:3px;height:3px;border-radius:50%;background:var(--gray-dark);display:block"></i>
    <i style="width:3px;height:3px;border-radius:50%;background:var(--gray-dark);display:block"></i>
  </div>
  <div class="photo" role="img" aria-label="Engineer in hard hat reading plans on a construction site" style="left:134px;top:0;width:163px;height:141px"></div>
  <div class="abs green" style="left:134px;top:141px;width:176px;height:33px;display:flex;align-items:center;justify-content:center">
    <span class="w" style="font-size:5.5px;letter-spacing:2.4px;margin-right:12px">WWW.WEBSITE.COM</span>
  </div>
</section>

<!-- 2 Agenda -->
<section class="slide c2 r1">
  <div class="photo" role="img" aria-label="Tall apartment building under a clear sky" style="left:42px;top:0;width:108px;height:174px"></div>
  <div class="abs green" style="left:27px;top:25px;width:29px;height:124px;display:flex;align-items:center;justify-content:center">
    <span class="w bold" style="transform:rotate(90deg);font-size:15px;white-space:nowrap">Agenda</span>
  </div>
  <div class="abs" style="left:166px;top:38px;width:130px">
    <div style="margin-bottom:9px"><div style="font-size:5.6px;font-weight:500">1. Lorem ipsum</div><div class="tiny" style="padding-left:8px">Company history and our founding in June 2020, mission and values</div></div>
    <div style="margin-bottom:9px"><div style="font-size:5.6px;font-weight:500">2. Lorem ipsum</div><div class="tiny" style="padding-left:8px">New affordable apartment buildings built from the ground up</div></div>
    <div style="margin-bottom:9px"><div style="font-size:5.6px;font-weight:500">3. Lorem ipsum</div><div class="tiny" style="padding-left:8px">Remodeling of apartment units and commercial buildings</div></div>
    <div><div style="font-size:5.6px;font-weight:500">4. Lorem ipsum</div><div class="tiny" style="padding-left:8px">Project timeline, our team and contact details</div></div>
  </div>
  <div class="stripe" style="left:305px;top:28px;width:5px;height:132px"></div>
  <div class="page">2</div>
</section>

<!-- 3 -->
<section class="slide c3 r1">
  <div class="stripe" style="left:0;top:29px;width:5px;height:132px"></div>
  <div class="abs" style="left:19px;top:52px;font-weight:700;font-size:19px;line-height:1.05">Text<br><span class="g">Added</span><br>Here</div>
  <div class="photo light" role="img" aria-label="Site manager reviewing a building frame under construction" style="left:99px;top:20px;width:211px;height:96px"></div>
  <div class="abs" style="left:136px;top:82px;width:62px;height:75px;background:#fff;box-shadow:0 1px 3px rgba(0,0,0,.15)"></div>
  <div class="abs" style="left:213px;top:82px;width:63px;height:75px;background:#fff;box-shadow:0 1px 3px rgba(0,0,0,.15)"></div>
  <div class="abs green w semi" style="left:138px;top:82px;width:58px;height:21px;font-size:9px;display:flex;align-items:center;justify-content:center">Text Here</div>
  <div class="abs green w semi" style="left:215px;top:82px;width:59px;height:21px;font-size:9px;display:flex;align-items:center;justify-content:center">Text Here</div>
  <div class="abs tiny" style="left:142px;top:107px;width:50px">We plan, permit and build quality apartments at prices families can afford.<br><br>Every project is managed on time and on budget.</div>
  <div class="abs tiny" style="left:219px;top:107px;width:50px">Our remodeling crews refresh units and commercial spaces with little downtime.<br><br>Clear quotes and honest schedules.</div>
  <div class="page">3</div>
</section>

<!-- 4 -->
<section class="slide c1 r2">
  <div class="stripe" style="left:0;top:0;width:9px;height:174px"></div>
  <div class="abs" style="left:29px;top:36px;font-weight:700;font-size:10.5px;line-height:1.2;width:110px">Lorem Ipsum<br>Dolor Sit<br>Ametkeeper.</div>
  <div class="abs" style="left:29px;top:77px;width:8px;height:1.4px;background:var(--ink)"></div>
  <div class="abs" style="left:39px;top:77px;width:3px;height:1.4px;background:var(--green)"></div>
  <div class="abs tiny" style="left:29px;top:83px;width:97px">Founded in June 2020, our company grew from a small remodeling crew into a general contractor trusted by owners, investors and property managers across the region.<br><br>We deliver new apartment buildings and renovations with safety and care.</div>
  <div class="abs" style="left:243px;top:22px;width:56px;height:40px;border-top:5px solid var(--green);border-right:5px solid var(--green)"></div>
  <div class="abs" style="left:139px;top:104px;width:56px;height:52px;border-bottom:5px solid var(--green);border-left:5px solid var(--green)"></div>
  <div class="photo light" role="img" aria-label="Two contractors reviewing plans inside a renovated room" style="left:151px;top:32px;width:140px;height:111px"></div>
  <div class="page">4</div>
</section>

<!-- 5 Part One -->
<section class="slide c2 r2">
  <div class="stripe" style="left:0;top:0;width:9px;height:174px"></div>
  <div class="abs" style="left:28px;top:60px;font-weight:600;font-size:15px">Part One</div>
  <div class="abs tiny" style="left:28px;top:79px;width:98px">Our story began in June 2020 with a focus on honest work and affordable housing for local communities.<br><br>Today we build new apartments and remodel units and commercial buildings.</div>
  <div class="photo" role="img" aria-label="Worker tying steel rebar on a concrete deck" style="left:169px;top:15px;width:121px;height:144px"></div>
  <div class="abs green" style="left:136px;top:53px;width:70px;height:69px;display:flex;align-items:center;justify-content:center;font-family:'Oswald',sans-serif;font-weight:700;font-size:46px;color:#fff">01</div>
  <div class="page">5</div>
</section>

<!-- 6 stats -->
<section class="slide c3 r2">
  <div class="stripe" style="left:0;top:10px;width:5px;height:52px"></div>
  <div class="abs" style="left:16px;top:12px;font-weight:700;font-size:12.5px;line-height:1.15">Lorem<br>Dolor Sit<br>Consectetuer</div>
  <div class="abs" style="left:180px;top:36px;width:52px">
    <div style="font-size:10px;font-weight:600">768K</div>
    <div class="g semi" style="font-size:5.5px">Lorem Ipsum</div>
    <div class="tiny">Square feet built and remodeled.</div>
  </div>
  <div class="abs" style="left:248px;top:36px;width:52px">
    <div style="font-size:10px;font-weight:600">423K</div>
    <div class="g semi" style="font-size:5.5px">Lorem Ipsum</div>
    <div class="tiny">Dollars saved for our clients.</div>
  </div>
  <div class="abs tiny" style="left:17px;top:72px;width:126px">We bring the same care to a single unit as to a full building, using trusted trades, clear budgets and steady site supervision from the first day to the final inspection.</div>
  <div class="abs w semi" style="left:177px;top:93px;width:133px;height:21px;background:var(--gray-dark);font-size:8.5px;display:flex;align-items:center;padding-left:9px">Text Added Here</div>
  <div class="stripe" style="left:69px;top:115px;width:7px;height:59px"></div>
  <div class="photo light" role="img" aria-label="Construction team standing on a building site" style="left:76px;top:115px;width:215px;height:59px"></div>
  <div class="page">6</div>
</section>

<!-- 7 bar chart -->
<section class="slide c1 r3">
  <div class="abs h-slide" style="left:16px;top:13px">Text<br>Added Hare<span class="accent"></span></div>
  <div class="abs" style="left:0;top:52px;width:100px;height:103px;background:var(--panel)"></div>
  <div class="abs" style="left:16px;top:62px;width:80px">
    <div style="display:flex;gap:4px;margin-bottom:11px"><span class="w bold" style="background:var(--gray-dark);width:10px;height:10px;font-size:6px;display:flex;align-items:center;justify-content:center;flex:none">1.</span><div><div class="semi" style="font-size:5.5px">Lorem ipsum</div><div class="tiny">New apartment buildings delivered on schedule</div></div></div>
    <div style="display:flex;gap:4px;margin-bottom:11px"><span class="w bold" style="background:var(--gray-dark);width:10px;height:10px;font-size:6px;display:flex;align-items:center;justify-content:center;flex:none">2.</span><div><div class="semi" style="font-size:5.5px">Lorem ipsum</div><div class="tiny">Apartment unit remodels completed each year</div></div></div>
    <div style="display:flex;gap:4px"><span class="w bold" style="background:var(--gray-dark);width:10px;height:10px;font-size:6px;display:flex;align-items:center;justify-content:center;flex:none">3.</span><div><div class="semi" style="font-size:5.5px">Lorem ipsum</div><div class="tiny">Commercial renovations for local owners</div></div></div>
  </div>
  <svg class="abs" style="left:108px;top:36px" width="190" height="130" viewBox="0 0 190 130" font-family="Poppins,sans-serif" font-size="4" fill="#555">
    <line x1="2" y1="98" x2="188" y2="98" stroke="#ddd" stroke-width=".6"/>
    <g>
      <rect x="13" y="24" width="4.5" height="74" fill="#79d94f"/><rect x="21" y="57" width="4.5" height="41" fill="#666"/><rect x="29" y="64" width="4.5" height="34" fill="#b9b9b9"/>
      <text x="9" y="21">43%</text><text x="18" y="54">24%</text><text x="28" y="61">20%</text>
      <rect x="60" y="55" width="4.5" height="43" fill="#79d94f"/><rect x="68" y="23" width="4.5" height="75" fill="#666"/><rect x="76" y="64" width="4.5" height="34" fill="#b9b9b9"/>
      <text x="57" y="52">25%</text><text x="66" y="20">44%</text><text x="75" y="61">20%</text>
      <rect x="107" y="38" width="4.5" height="60" fill="#79d94f"/><rect x="115" y="67" width="4.5" height="31" fill="#666"/><rect x="123" y="47" width="4.5" height="51" fill="#b9b9b9"/>
      <text x="104" y="35">35%</text><text x="113" y="64">18%</text><text x="121" y="44">30%</text>
      <rect x="154" y="21" width="4.5" height="77" fill="#79d94f"/><rect x="162" y="50" width="4.5" height="48" fill="#666"/><rect x="170" y="13" width="4.5" height="85" fill="#b9b9b9"/>
      <text x="150" y="18">45%</text><text x="160" y="47">28%</text><text x="169" y="10">50%</text>
    </g>
    <text x="22" y="106">1</text><text x="69" y="106">2</text><text x="116" y="106">3</text><text x="163" y="106">4</text>
    <rect x="61" y="112" width="2" height="2" fill="#79d94f"/><text x="64" y="114.5" font-size="3.5">Series1</text>
    <rect x="83" y="112" width="2" height="2" fill="#666"/><text x="86" y="114.5" font-size="3.5">Series2</text>
    <rect x="105" y="112" width="2" height="2" fill="#b9b9b9"/><text x="108" y="114.5" font-size="3.5">Series3</text>
  </svg>
  <div class="stripe" style="left:305px;top:20px;width:5px;height:145px"></div>
  <div class="page">7</div>
</section>

<!-- 8 donuts -->
<section class="slide c2 r3">
  <div class="stripe" style="left:0;top:20px;width:5px;height:137px"></div>
  <div class="abs h-slide" style="left:0;width:310px;top:12px;text-align:center;font-size:10px">Text Added Hare</div>
  <div class="abs" style="left:143px;top:27px;width:8px;height:1.4px;background:var(--green)"></div>
  <div class="abs" style="left:153px;top:27px;width:3px;height:1.4px;background:var(--ink)"></div>
  <div class="abs tiny" style="left:55px;top:37px;width:200px;text-align:center">Since June 2020 our crews have completed new affordable apartment buildings, unit remodels and commercial upgrades. We measure success by on time delivery, budget accuracy and the satisfaction of every owner and resident.</div>
  <svg class="abs" style="left:0;top:68px" width="310" height="65" viewBox="0 0 310 65" font-family="Poppins,sans-serif">
    <g transform="translate(75,31)">
      <circle r="24" fill="none" stroke="#eee" stroke-width="4.5"/>
      <circle r="24" fill="none" stroke="#79d94f" stroke-width="4.5" stroke-dasharray="75.4 150.8" transform="rotate(-90)"/>
      <text y="4.5" text-anchor="middle" font-size="13" font-weight="500" fill="#2b2b2b">50%</text>
    </g>
    <g transform="translate(155,31)">
      <circle r="24" fill="none" stroke="#eee" stroke-width="4.5"/>
      <circle r="24" fill="none" stroke="#666" stroke-width="4.5" stroke-dasharray="113.1 150.8" transform="rotate(-90)"/>
      <text y="4.5" text-anchor="middle" font-size="13" font-weight="500" fill="#2b2b2b">75%</text>
    </g>
    <g transform="translate(235,31)">
      <circle r="24" fill="none" stroke="#eee" stroke-width="4.5"/>
      <circle r="24" fill="none" stroke="#b9b9b9" stroke-width="4.5" stroke-dasharray="60.3 150.8" transform="rotate(-90)"/>
      <text y="4.5" text-anchor="middle" font-size="13" font-weight="500" fill="#2b2b2b">40%</text>
    </g>
  </svg>
  <div class="abs tiny" style="left:45px;top:136px;width:60px;text-align:center">New builds on schedule ahead of plan</div>
  <div class="abs tiny" style="left:125px;top:136px;width:60px;text-align:center">Remodels finished under budget</div>
  <div class="abs tiny" style="left:205px;top:136px;width:60px;text-align:center">Repeat clients from commercial work</div>
  <div class="page">8</div>
</section>

<!-- 9 cycle -->
<section class="slide c3 r3">
  <div class="abs h-slide" style="left:16px;top:13px">Text<br>Added Hare<span class="accent"></span></div>
  <div class="abs tiny" style="left:16px;top:50px;width:88px">We guide each project through clear steps from first visit to final handover.<br><br>Every stage has one manager, one schedule and one budget you can follow.</div>
  <div class="abs green" style="left:0;top:98px;width:99px;height:58px;padding:7px 0 0 8px">
    <div style="display:flex;gap:4px;margin-bottom:6px"><i style="width:4px;height:4px;border-radius:50%;background:#fff;flex:none;margin-top:2px;display:block"></i><div><div class="w semi" style="font-size:5px">Lorem Ipsum</div><div class="w" style="font-size:3.1px;line-height:1.3">Site review, estimate and permits prepared for approval</div></div></div>
    <div style="display:flex;gap:4px"><i style="width:4px;height:4px;border-radius:50%;background:#fff;flex:none;margin-top:2px;display:block"></i><div><div class="w semi" style="font-size:5px">Lorem Ipsum</div><div class="w" style="font-size:3.1px;line-height:1.3">Build, inspect and hand over keys with full warranty</div></div></div>
  </div>
  <svg class="abs" style="left:120px;top:20px" width="190" height="145" viewBox="0 0 190 145" font-family="Poppins,sans-serif">
    <path d="M125 15 A58 58 0 1 0 104 128" fill="none" stroke="#333" stroke-width="2.2"/>
    <path d="M16 55 L20 65 L25 55" fill="none" stroke="#333" stroke-width="2.2" stroke-linecap="round"/>
    <path d="M125 15 A32 32 0 0 1 127 98" fill="none" stroke="#333" stroke-width="2.2"/>
    <circle cx="134" cy="36" r="19" fill="#79d94f"/><circle cx="134" cy="36" r="14" fill="#fff"/>
    <circle cx="132" cy="34" r="4" fill="none" stroke="#333" stroke-width="1.2"/><line x1="135" y1="37" x2="138" y2="40" stroke="#333" stroke-width="1.2"/>
    <circle cx="143" cy="84" r="13" fill="#79d94f"/><circle cx="143" cy="84" r="9" fill="#fff"/><circle cx="143" cy="84" r="3" fill="#333"/>
    <circle cx="108" cy="117" r="10" fill="#79d94f"/><circle cx="108" cy="117" r="7" fill="#fff"/><path d="M108 113 v7 M105 118 q3 3 6 0" stroke="#333" stroke-width="1" fill="none"/>
    <circle cx="43" cy="103" r="10" fill="#79d94f"/><circle cx="43" cy="103" r="7" fill="#fff"/><rect x="40.5" y="101" width="5" height="5" rx="1" fill="#333"/>
    <circle cx="20" cy="84" r="3" fill="#333"/><line x1="20" y1="87" x2="36" y2="98" stroke="#333" stroke-width="1.4"/>
    <rect x="62" y="52" width="2" height="8" fill="#79d94f"/><rect x="65" y="49" width="2" height="11" fill="#333"/><rect x="68" y="54" width="2" height="6" fill="#79d94f"/><rect x="61" y="60" width="11" height="1" fill="#333"/>
    <text x="66" y="68" text-anchor="middle" font-size="5" font-weight="600" fill="#2b2b2b">MAIN TITLE</text>
    <text x="66" y="73" text-anchor="middle" font-size="3" fill="#8a8a8a">Plan, build and deliver</text>
    <text x="66" y="77" text-anchor="middle" font-size="3" fill="#8a8a8a">each home with care</text>
    <line x1="153" y1="25" x2="161" y2="21" stroke="#79d94f" stroke-width=".6"/><text x="163" y="22" font-size="3.4" fill="#333">85%</text>
    <text x="164" y="32" font-size="4.4" font-weight="600" fill="#2b2b2b">Your Title</text>
    <text x="160" y="37" font-size="2.6" fill="#8a8a8a">Estimate and permits</text>
    <text x="168" y="79" font-size="4.4" font-weight="600" fill="#2b2b2b">Your Title</text>
    <text x="165" y="84" font-size="2.6" fill="#8a8a8a">Framing and systems</text>
    <line x1="122" y1="80" x2="130" y2="82" stroke="#79d94f" stroke-width=".6"/><text x="112" y="80" font-size="3.4" fill="#333">80%</text>
    <text x="158" y="118" font-size="4.4" font-weight="600" fill="#2b2b2b">Your Title</text>
    <text x="155" y="123" font-size="2.6" fill="#8a8a8a">Inspection and finish</text>
    <line x1="116" y1="123" x2="124" y2="127" stroke="#79d94f" stroke-width=".6"/><text x="125" y="129" font-size="3.4" fill="#333">75%</text>
    <text x="2" y="100" font-size="4.4" font-weight="600" fill="#2b2b2b">Your Title</text>
    <text x="0" y="105" font-size="2.6" fill="#8a8a8a">First site visit</text>
    <line x1="53" y1="100" x2="61" y2="98" stroke="#79d94f" stroke-width=".6"/><text x="62" y="99" font-size="3.4" fill="#333">50%</text>
  </svg>
  <div class="page">9</div>
</section>

<!-- 10 Service -->
<section class="slide c1 r4">
  <div class="abs green" style="left:8px;top:8px;width:58px;height:54px"></div>
  <div class="photo" role="img" aria-label="Glass office towers seen from below" style="left:20px;top:19px;width:116px;height:137px"></div>
  <div class="abs green w semi" style="left:44px;top:125px;width:68px;height:20px;font-size:10px;display:flex;align-items:center;justify-content:center">Service</div>
  <div class="abs" style="left:153px;top:33px;width:140px">
    <div style="display:flex;gap:7px;margin-bottom:19px;align-items:flex-start"><span style="width:24px;height:24px;border-radius:50%;background:var(--gray-dark);flex:none;display:flex;align-items:center;justify-content:center"><svg width="12" height="12" viewBox="0 0 12 12"><circle cx="6" cy="6" r="4.5" fill="none" stroke="#fff" stroke-width="1"/><circle cx="6" cy="6" r="2" fill="none" stroke="#fff" stroke-width="1"/><line x1="6" y1="6" x2="11" y2="1" stroke="#fff" stroke-width="1"/></svg></span><div><div class="g semi" style="font-size:6.5px">Project name</div><div class="tiny">New affordable apartment buildings planned and built from the ground up.</div></div></div>
    <div style="display:flex;gap:7px;margin-bottom:19px;align-items:flex-start"><span style="width:24px;height:24px;border-radius:50%;background:var(--gray-dark);flex:none;display:flex;align-items:center;justify-content:center"><svg width="12" height="12" viewBox="0 0 12 12"><circle cx="6" cy="6" r="4.5" fill="none" stroke="#fff" stroke-width="1"/><circle cx="6" cy="6" r="2" fill="none" stroke="#fff" stroke-width="1"/><line x1="6" y1="6" x2="11" y2="1" stroke="#fff" stroke-width="1"/></svg></span><div><div class="g semi" style="font-size:6.5px">Project name</div><div class="tiny">Remodeling of apartment units with modern kitchens, baths and floors.</div></div></div>
    <div style="display:flex;gap:7px;align-items:flex-start"><span style="width:24px;height:24px;border-radius:50%;background:var(--gray-dark);flex:none;display:flex;align-items:center;justify-content:center"><svg width="12" height="12" viewBox="0 0 12 12"><circle cx="6" cy="6" r="4.5" fill="none" stroke="#fff" stroke-width="1"/><circle cx="6" cy="6" r="2" fill="none" stroke="#fff" stroke-width="1"/><line x1="6" y1="6" x2="11" y2="1" stroke="#fff" stroke-width="1"/></svg></span><div><div class="g semi" style="font-size:6.5px">Project name</div><div class="tiny">Commercial building renovations for offices, shops and mixed use.</div></div></div>
  </div>
  <div class="stripe" style="left:305px;top:20px;width:5px;height:135px"></div>
  <div class="page">10</div>
</section>

<!-- 11 SWOT -->
<section class="slide c2 r4">
  <div class="abs h-slide" style="left:13px;top:8px;font-size:10px">Text Added Hare<span class="accent"></span></div>
  <svg class="abs" style="left:0;top:0" width="310" height="174" viewBox="0 0 310 174" font-family="Poppins,sans-serif">
    <line x1="155" y1="38" x2="155" y2="150" stroke="#999" stroke-width=".8" stroke-dasharray="1 1.5"/>
    <line x1="100" y1="93" x2="210" y2="93" stroke="#999" stroke-width=".8" stroke-dasharray="1 1.5"/>
    <circle cx="131" cy="70" r="20" fill="#6a6a6a"/><circle cx="179" cy="70" r="20" fill="#6a6a6a"/>
    <circle cx="131" cy="118" r="20" fill="#6a6a6a"/><circle cx="179" cy="118" r="20" fill="#6a6a6a"/>
    <g font-size="18" font-style="italic" font-weight="500" fill="#fff" text-anchor="middle">
      <text x="131" y="76">S</text><text x="179" y="76">W</text><text x="131" y="124">O</text><text x="179" y="124">T</text>
    </g>
    <ellipse cx="155" cy="93" rx="19" ry="12" fill="#79d94f"/>
    <text x="155" y="95" text-anchor="middle" font-size="4.6" font-style="italic" fill="#2b2b2b">ANALYSIS</text>
    <g font-size="4" font-style="italic" fill="#5fc23a">
      <text x="76" y="44">STRENGTHS</text><text x="203" y="42">WEAKNESSES</text>
      <text x="73" y="110">OPPORTUNITIES</text><text x="207" y="107">THREATS</text>
    </g>
    <g font-size="2.7" fill="#777">
      <text x="77" y="50">• Local crews</text><text x="77" y="56">• Fair pricing</text><text x="77" y="62">• Many trades</text><text x="77" y="68">• Fast permits</text>
      <text x="204" y="48">• Young company</text><text x="204" y="54">• Small fleet of</text><text x="206" y="58">equipment</text><text x="204" y="64">• Limited brand</text><text x="206" y="68">reach so far</text>
      <text x="74" y="116">• Growing need for</text><text x="76" y="120">affordable homes</text><text x="74" y="127">• Aging buildings</text><text x="76" y="131">ready to remodel</text><text x="76" y="135">across the city</text>
      <text x="208" y="113">• Rising material</text><text x="210" y="117">costs</text><text x="208" y="123">• Labor shortages</text><text x="208" y="129">• New competitors</text><text x="210" y="133">in the area</text>
    </g>
  </svg>
  <div class="stripe" style="left:305px;top:20px;width:5px;height:135px"></div>
  <div class="page">11</div>
</section>

<!-- 12 -->
<section class="slide c3 r4">
  <div class="stripe" style="left:0;top:22px;width:4px;height:132px"></div>
  <svg class="abs" style="left:0;top:0" width="175" height="174" viewBox="0 0 175 174">
    <circle cx="67" cy="87" r="41" fill="none" stroke="#6a6a6a" stroke-width="3"/>
    <circle cx="67" cy="87" r="37" fill="none" stroke="#6a6a6a" stroke-width="1.5"/>
    <circle cx="67" cy="87" r="33" fill="#79d94f"/>
    <polyline points="110,70 124,44 150,44" fill="none" stroke="#333" stroke-width=".8"/>
    <line x1="117" y1="87" x2="150" y2="87" stroke="#333" stroke-width=".8"/>
    <polyline points="110,104 124,130 150,130" fill="none" stroke="#333" stroke-width=".8"/>
  </svg>
  <div class="abs w semi" style="left:34px;top:69px;width:66px;text-align:center;font-size:11px;line-height:1.15">Text<br>Added<br>Hare</div>
  <div class="abs" style="left:158px;top:31px;width:145px">
    <div style="display:flex;gap:7px;margin-bottom:16px"><span style="width:26px;height:26px;border-radius:50%;background:var(--green);flex:none;display:flex;align-items:center;justify-content:center"><svg width="13" height="13" viewBox="0 0 12 12"><circle cx="6" cy="6" r="4.5" fill="none" stroke="#fff" stroke-width="1"/><circle cx="6" cy="6" r="2" fill="none" stroke="#fff" stroke-width="1"/><line x1="6" y1="6" x2="11" y2="1" stroke="#fff" stroke-width="1"/></svg></span><div><div class="semi" style="font-size:6.5px">Project name</div><div class="tiny">Forty unit affordable apartment building delivered ahead of schedule.</div></div></div>
    <div style="display:flex;gap:7px;margin-bottom:16px"><span style="width:26px;height:26px;border-radius:50%;background:var(--green);flex:none;display:flex;align-items:center;justify-content:center"><svg width="13" height="13" viewBox="0 0 12 12"><circle cx="6" cy="6" r="4.5" fill="none" stroke="#fff" stroke-width="1"/><circle cx="6" cy="6" r="2" fill="none" stroke="#fff" stroke-width="1"/><line x1="6" y1="6" x2="11" y2="1" stroke="#fff" stroke-width="1"/></svg></span><div><div class="semi" style="font-size:6.5px">Project name</div><div class="tiny">Full remodel of thirty apartment units while residents stayed home.</div></div></div>
    <div style="display:flex;gap:7px"><span style="width:26px;height:26px;border-radius:50%;background:var(--green);flex:none;display:flex;align-items:center;justify-content:center"><svg width="13" height="13" viewBox="0 0 12 12"><circle cx="6" cy="6" r="4.5" fill="none" stroke="#fff" stroke-width="1"/><circle cx="6" cy="6" r="2" fill="none" stroke="#fff" stroke-width="1"/><line x1="6" y1="6" x2="11" y2="1" stroke="#fff" stroke-width="1"/></svg></span><div><div class="semi" style="font-size:6.5px">Project name</div><div class="tiny">Retail storefront and office floor renovation on a tight timeline.</div></div></div>
  </div>
  <div class="page">12</div>
</section>

<!-- 13 Timeline -->
<section class="slide c1 r5">
  <div class="abs w bold" style="left:0;top:13px;width:163px;height:18px;background:#333;font-size:11px;display:flex;align-items:center;padding-left:15px">Project Timeline - 2024</div>
  <svg class="abs" style="left:0;top:0" width="310" height="174" viewBox="0 0 310 174" font-family="Poppins,sans-serif">
    <polygon points="39,91 84,91 79,100 34,100" fill="#79d94f"/>
    <polygon points="89,91 131,91 126,100 84,100" fill="#333"/>
    <polygon points="131,91 176,91 171,100 126,100" fill="#79d94f"/>
    <polygon points="181,91 223,91 218,100 176,100" fill="#333"/>
    <polygon points="223,91 268,91 263,100 218,100" fill="#79d94f"/>
    <g font-size="4" fill="#fff" text-anchor="middle" font-weight="500">
      <text x="58" y="97">1990</text><text x="105" y="97">2001</text><text x="151" y="97">2007</text><text x="197" y="97">2012</text><text x="243" y="97">2020</text>
    </g>
    <g stroke="#79d94f" stroke-width=".9"><line x1="58" y1="80" x2="58" y2="89"/><line x1="151" y1="80" x2="151" y2="89"/><line x1="243" y1="80" x2="243" y2="89"/></g>
    <g fill="#79d94f"><circle cx="58" cy="79" r="1.5"/><circle cx="151" cy="79" r="1.5"/><circle cx="243" cy="79" r="1.5"/></g>
    <g stroke="#333" stroke-width=".9"><line x1="104" y1="102" x2="104" y2="111"/><line x1="196" y1="102" x2="196" y2="111"/></g>
    <g fill="#333"><circle cx="104" cy="112" r="1.5"/><circle cx="196" cy="112" r="1.5"/></g>
    <g text-anchor="middle">
      <text x="58" y="58" font-size="4.6" font-weight="600" fill="#2b2b2b">Your Title</text>
      <text x="58" y="63" font-size="3.3" fill="#888">Refers to a good or</text><text x="58" y="67" font-size="3.3" fill="#888">service being offered</text>
      <text x="151" y="58" font-size="4.6" font-weight="600" fill="#2b2b2b">Your Title</text>
      <text x="151" y="63" font-size="3.3" fill="#888">Refers to a good or</text><text x="151" y="67" font-size="3.3" fill="#888">service being offered</text>
      <text x="243" y="58" font-size="4.6" font-weight="600" fill="#2b2b2b">Your Title</text>
      <text x="243" y="63" font-size="3.3" fill="#888">Refers to a good or</text><text x="243" y="67" font-size="3.3" fill="#888">service being offered</text>
      <text x="104" y="127" font-size="4.6" font-weight="600" fill="#2b2b2b">Your Title</text>
      <text x="104" y="132" font-size="3.3" fill="#888">Refers to a good or</text><text x="104" y="136" font-size="3.3" fill="#888">service being offered</text>
      <text x="196" y="127" font-size="4.6" font-weight="600" fill="#2b2b2b">Your Title</text>
      <text x="196" y="132" font-size="3.3" fill="#888">Refers to a good or</text><text x="196" y="136" font-size="3.3" fill="#888">service being offered</text>
    </g>
  </svg>
  <div class="page">13</div>
</section>

<!-- 14 -->
<section class="slide c2 r5">
  <div class="photo" role="img" aria-label="Office building facade in grey tones" style="left:0;top:0;width:109px;height:174px"></div>
  <div class="abs w bold" style="left:19px;top:28px;width:14px;height:110px;display:flex;align-items:center;justify-content:center">
    <span style="transform:rotate(90deg);white-space:nowrap;font-size:10px;letter-spacing:3.5px">TEXT ADDED</span>
  </div>
  <div class="abs green w bold" style="left:60px;top:27px;width:110px;height:32px;font-size:9.5px;display:flex;align-items:center;padding-left:14px;box-shadow:0 2px 3px rgba(0,0,0,.2)">1. Lorem Ipsum</div>
  <div class="abs green w bold" style="left:60px;top:72px;width:110px;height:32px;font-size:9.5px;display:flex;align-items:center;padding-left:14px;box-shadow:0 2px 3px rgba(0,0,0,.2)">2. Lorem Ipsum</div>
  <div class="abs green w bold" style="left:60px;top:124px;width:110px;height:32px;font-size:9.5px;display:flex;align-items:center;padding-left:14px;box-shadow:0 2px 3px rgba(0,0,0,.2)">3. Lorem Ipsum</div>
  <div class="abs h-slide" style="left:191px;top:50px">Text<br>Added Hare<span class="accent"></span></div>
  <div class="abs tiny" style="left:191px;top:88px;width:92px">Three things guide every job we take on.<br><br>Quality work from trusted trades, honest pricing that fits real budgets and schedules we keep from start to finish.</div>
  <div class="page">14</div>
</section>

<!-- 15 process -->
<section class="slide c3 r5">
  <div class="abs h-slide" style="left:12px;top:8px;font-size:10px">Text Added Hare<span class="accent"></span></div>
  <svg class="abs" style="left:0;top:0" width="310" height="174" viewBox="0 0 310 174" font-family="Poppins,sans-serif">
    <rect x="20" y="92" width="71" height="4" fill="#6a6a6a"/>
    <rect x="91" y="92" width="54" height="4" fill="#79d94f"/>
    <rect x="145" y="92" width="54" height="4" fill="#6a6a6a"/>
    <rect x="199" y="92" width="80" height="4" fill="#79d94f"/>
    <polygon points="279,89 285,94 279,99" fill="#79d94f"/>
    <g font-size="3.4" fill="#fff" text-anchor="middle" font-weight="600"><text x="71" y="95.3">Step 01</text><text x="125" y="95.3">Step 02</text><text x="179" y="95.3">Step 03</text><text x="240" y="95.3">Step 04</text></g>
    <g fill="none" stroke-width="4.5"><path d="M55 92 A18 18 0 1 1 89 92" stroke="#6a6a6a"/><path d="M109 92 A18 18 0 1 1 143 92" stroke="#79d94f"/><path d="M163 92 A18 18 0 1 1 197 92" stroke="#6a6a6a"/><path d="M218 92 A18 18 0 1 1 252 92" stroke="#79d94f"/></g>
    <g fill="#fff" stroke="#333" stroke-width="1"><circle cx="72" cy="78" r="6"/></g>
    <path d="M72 74 v4 h3" stroke="#333" stroke-width="1" fill="none"/>
    <circle cx="126" cy="79" r="5" fill="#333"/><text x="126" y="81" font-size="5.5" fill="#fff" text-anchor="middle" font-weight="700">$</text>
    <g fill="none" stroke="#333" stroke-width="1"><ellipse cx="180" cy="74" rx="5" ry="1.8"/><path d="M175 74 v8 a5 1.8 0 0 0 10 0 v-8"/><path d="M175 78 a5 1.8 0 0 0 10 0"/></g>
    <circle cx="234" cy="77" r="4" fill="none" stroke="#333" stroke-width="1.3"/><line x1="231" y1="80" x2="228" y2="84" stroke="#333" stroke-width="1.5"/>
    <g stroke="#666" stroke-width=".7"><line x1="71" y1="100" x2="71" y2="108"/><line x1="125" y1="100" x2="125" y2="108"/><line x1="179" y1="100" x2="179" y2="108"/><line x1="234" y1="100" x2="234" y2="108"/></g>
    <g text-anchor="middle">
      <g font-size="5.6" font-weight="600" fill="#2b2b2b"><text x="71" y="118">Lorem Ipsum</text><text x="125" y="118">Lorem Ipsum</text><text x="179" y="118">Lorem Ipsum</text><text x="234" y="118">Lorem Ipsum</text></g>
      <g font-size="2.7" fill="#888">
        <text x="71" y="123">Meet on site and walk</text><text x="71" y="126.5">the property together</text><text x="71" y="130">to review the goals</text>
        <text x="125" y="123">Receive a clear and</text><text x="125" y="126.5">detailed estimate with</text><text x="125" y="130">a fixed budget</text>
        <text x="179" y="123">Order materials and</text><text x="179" y="126.5">schedule the trades</text><text x="179" y="130">for every phase</text>
        <text x="234" y="123">Final walkthrough,</text><text x="234" y="126.5">inspection and keys</text><text x="234" y="130">handed to owner</text>
      </g>
    </g>
  </svg>
  <div class="page">15</div>
</section>

<!-- 16 -->
<section class="slide c1 r6">
  <div class="abs" role="img" aria-label="Faint world map in the background" style="left:150px;top:45px;width:150px;height:100px;background:radial-gradient(ellipse at center,#ececec 0%,#f6f6f6 60%,#fff 100%)"></div>
  <div class="abs" style="left:20px;top:27px;font-weight:700;font-size:15.5px;line-height:1.1">Text<br><span class="g">Added</span><br>Here</div>
  <div class="abs green" style="left:0;top:89px;width:116px;height:67px;padding:7px 0 0 20px">
    <div style="display:flex;gap:4px;margin-bottom:5px"><span class="w bold" style="background:var(--ink);width:10px;height:10px;font-size:6px;display:flex;align-items:center;justify-content:center;flex:none">1.</span><div><div class="semi" style="font-size:5px;color:var(--ink)">Lorem Ipsum</div><div style="font-size:2.9px;line-height:1.3;color:var(--ink)">Track progress on your phone every day</div></div></div>
    <div style="display:flex;gap:4px;margin-bottom:5px"><span class="w bold" style="background:var(--ink);width:10px;height:10px;font-size:6px;display:flex;align-items:center;justify-content:center;flex:none">2.</span><div><div class="semi" style="font-size:5px;color:var(--ink)">Lorem Ipsum</div><div style="font-size:2.9px;line-height:1.3;color:var(--ink)">Photos and updates sent after each visit</div></div></div>
    <div style="display:flex;gap:4px"><span class="w bold" style="background:var(--ink);width:10px;height:10px;font-size:6px;display:flex;align-items:center;justify-content:center;flex:none">3.</span><div><div class="semi" style="font-size:5px;color:var(--ink)">Lorem Ipsum</div><div style="font-size:2.9px;line-height:1.3;color:var(--ink)">Approve changes and invoices online</div></div></div>
  </div>
  <div class="abs" style="left:139px;top:26px;width:38px;height:80px;border:1.3px solid var(--ink);border-radius:4px;background:#fff;padding:14px 3px 0">
    <div class="abs" style="left:13px;top:2px;width:10px;height:2px;background:var(--ink);border-radius:1px"></div>
    <div style="font-size:4px;line-height:1.1;font-weight:500">Lorem<br>ipsum dolor</div>
    <div style="width:10px;height:8px;border:.8px solid var(--green);margin:8px auto 6px"></div>
    <div style="font-size:2.4px;line-height:1.3;color:#555">Plan your home project with our team and see each step from start to finish.</div>
  </div>
  <div class="abs" style="left:187px;top:50px;width:37px;height:78px;border:1.3px solid var(--ink);border-radius:4px;background:#fff;padding:14px 3px 0">
    <div class="abs" style="left:13px;top:2px;width:10px;height:2px;background:var(--ink);border-radius:1px"></div>
    <div style="font-size:4px;line-height:1.1;font-weight:500">Dolor sit<br>amet, conse</div>
    <div style="width:9px;height:9px;border:.8px solid var(--green);border-radius:50%;margin:6px auto 5px"></div>
    <div style="font-size:2.4px;line-height:1.3;color:#555">Get weekly updates, photos and notes from your site manager.</div>
  </div>
  <div class="abs" style="left:235px;top:76px;width:37px;height:79px;border:1.3px solid var(--ink);border-radius:4px;background:#fff;padding:14px 3px 0">
    <div class="abs" style="left:13px;top:2px;width:10px;height:2px;background:var(--ink);border-radius:1px"></div>
    <div style="font-size:4px;font-weight:500">Consec</div>
    <div style="font-size:4px;color:var(--green);letter-spacing:1px">• • • • •</div>
    <div style="width:10px;height:10px;border:.8px solid var(--green);border-radius:50%;margin:6px auto 5px"></div>
    <div style="font-size:2.4px;line-height:1.3;color:#555">Rate your experience after each finished project phase.</div>
  </div>
  <div class="page">16</div>
</section>

<!-- 17 Team -->
<section class="slide c2 r6">
  <div class="abs h-slide" style="left:13px;top:8px;font-size:10px">Text Added Hare<span class="accent"></span></div>
  <div class="abs" style="left:30px;top:58px;width:46px;height:17px;background:var(--green)"></div>
  <div class="abs" style="left:97px;top:58px;width:46px;height:17px;background:#6a6a6a"></div>
  <div class="abs" style="left:166px;top:58px;width:46px;height:17px;background:var(--green)"></div>
  <div class="abs" style="left:237px;top:58px;width:46px;height:17px;background:#6a6a6a"></div>
  <div class="abs photo light" role="img" aria-label="Team member portrait" style="left:41px;top:63px;width:24px;height:24px;border-radius:50%;border:1.5px solid #fff"></div>
  <div class="abs photo light" role="img" aria-label="Team member portrait" style="left:108px;top:63px;width:24px;height:24px;border-radius:50%;border:1.5px solid #fff"></div>
  <div class="abs photo light" role="img" aria-label="Team member portrait" style="left:177px;top:63px;width:24px;height:24px;border-radius:50%;border:1.5px solid #fff"></div>
  <div class="abs photo light" role="img" aria-label="Team member portrait" style="left:248px;top:63px;width:24px;height:24px;border-radius:50%;border:1.5px solid #fff"></div>
  <div class="abs" style="left:23px;top:93px;width:60px;text-align:center"><div class="semi" style="font-size:5.5px">JOHN SMITH</div><div class="tiny" style="font-size:2.8px">Founder and general contractor leading every build.<br><br>Licensed builder since 2020.</div></div>
  <div class="abs" style="left:90px;top:93px;width:60px;text-align:center"><div class="semi g" style="font-size:5.5px">MILLIE SMITH</div><div class="tiny" style="font-size:2.8px">Project manager for apartment remodels and budgets.<br><br>Keeps owners informed.</div></div>
  <div class="abs" style="left:159px;top:93px;width:60px;text-align:center"><div class="semi" style="font-size:5.5px">JOHN SMITH</div><div class="tiny" style="font-size:2.8px">Site superintendent for new ground up construction.<br><br>Safety comes first.</div></div>
  <div class="abs" style="left:230px;top:93px;width:60px;text-align:center"><div class="semi g" style="font-size:5.5px">MILLIE SMITH</div><div class="tiny" style="font-size:2.8px">Estimator for commercial building renovations.<br><br>Clear and fair quotes.</div></div>
  <div class="page">17</div>
</section>

<!-- 18 Closing -->
<section class="slide c3 r6">
  <div class="photo light" role="img" aria-label="Faded view of a modern glass building" style="left:0;top:0;width:310px;height:174px;background:linear-gradient(135deg,#f4f4f4,#e0e0e0 50%,#cfcfcf)"></div>
  <div class="abs" style="left:40px;top:82px;display:flex;align-items:center;gap:4px">
    <span style="width:8px;height:8px;background:var(--green);display:block"></span>
    <span style="font-size:7px;font-weight:600;color:var(--ink)">R3 Construction Corp.</span>
  </div>
  <div class="abs green" style="left:148px;top:67px;width:162px;height:57px;padding:5px 0 0 9px;color:var(--ink)">
    <div class="semi" style="font-size:6.8px;line-height:1.2">R3 Construction Corp.</div>
    <div style="font-size:5.8px;font-style:italic;line-height:1.3">4870 Linden Ave. Suite 212<br>Maple Grove, CA 91550<br>555-014-2237</div>
    <div style="font-size:6.5px;line-height:1.3">LICENSE NO. 2046815</div>
  </div>
</section>

</div>
</body>
</html>
```